Higher co-efficient of performance means more heat for your money

I need a bar graph that will have the following heating systems, 80% efficient gas furnace COP of .8, Electric heat COP of 1, and Our best selling heat pump with a cop of 4 at 47F. I will have a constant bar, 100$ worth of gas for furnace, 100$ of electricity for electric heat, and 100$ worth of electricity for our heat pumps. next to them I will have a bar showing how much heat each heating system will provide for $100 of fuel. For gas furnace I need a bar that says $80 worth of heat and the barograph to match it, for electric heat I need the bar to show 100$ worth of heat, for our best selling heat pump I need the bar graph to show and say $400 dollars worth of heat. Please take a look at my website www.brightmarkcomfort.example for brand color and feel

```html
<!DOCTYPE html>
<html lang="en">
<head>
<meta charset="utf-8">
<title>More heat for your money</title>
<link rel="stylesheet" href="https://fonts.googleapis.com/css2?family=Saira+Semi+Condensed:wght@400;500;600&display=swap">
<style>
  :root {
    --bg-light: #f1f1f2;
    --bg-mid: #e2e2e4;
    --axis-grey: #8d8d90;
    --grid: #d9d9dc;
    --brand-blue: #1d6bb5;
    --brand-red: #c8202a;
    --fuel-top: #2a78a6;
    --fuel-bottom: #84d3e2;
    --heat-top: #c8202a;
    --heat-bottom: #f0891d;
    --ghost: #f7f7f8;
    --label-white: #ffffff;
  }
  html, body {
    margin: 0;
    padding: 0;
    overflow: hidden;
  }
  body {
    width: 1200px;
    height: 843px;
    font-family: "Saira Semi Condensed", sans-serif;
  }
  .poster {
    position: relative;
    width: 1200px;
    height: 843px;
    background:
      radial-gradient(ellipse at 55% 40%, var(--bg-light) 0%, transparent 65%),
      linear-gradient(180deg, var(--bg-mid), var(--bg-light) 50%, var(--bg-mid));
    overflow: hidden;
  }
  .chart {
    position: absolute;
    inset: 0;
  }
  .axis-label {
    font-size: 19px;
    fill: var(--axis-grey);
    font-weight: 500;
  }
  .grid-line {
    stroke: var(--grid);
    stroke-width: 1;
  }
  .bar-label {
    font-size: 13.5px;
    fill: var(--label-white);
    font-weight: 500;
    letter-spacing: 0.3px;
  }
  .bar-label--large {
    font-size: 40px;
    font-weight: 500;
    letter-spacing: 1px;
  }
  .category {
    font-size: 18px;
    fill: var(--brand-blue);
    font-weight: 500;
    text-anchor: middle;
  }
  .brand {
    position: absolute;
    left: 930px;
    top: 150px;
    width: 210px;
    display: flex;
    align-items: center;
    justify-content: center;
    gap: 8px;
    color: var(--brand-blue);
    font-size: 24px;
    font-weight: 600;
    white-space: nowrap;
  }
  .brand-dot {
    width: 14px;
    height: 14px;
    border-radius: 50%;
    background: var(--brand-blue);
  }
  .callout {
    position: absolute;
    left: 922px;
    top: 254px;
    width: 210px;
    height: 114px;
  }
  .callout-bracket {
    position: absolute;
    width: 22px;
    height: 20px;
    border-color: var(--brand-red);
    border-style: solid;
  }
  .callout-bracket--top { left: 0; top: 0; border-width: 3px 0 0 3px; }
  .callout-bracket--bottom { right: 0; bottom: 0; border-width: 0 3px 3px 0; }
  .callout-text {
    margin: 9px 0 0 14px;
    text-align: center;
    color: var(--brand-blue);
    font-size: 18.5px;
    line-height: 23px;
    font-weight: 500;
  }
  .callout-note {
    display: block;
    font-size: 9.5px;
    line-height: 10px;
    margin-top: -1px;
  }
</style>
</head>
<body>
<div class="poster">
  <svg class="chart" width="1200" height="843" viewBox="0 0 1200 843" aria-label="Bar chart comparing heat delivered per $100 of fuel">
    <defs>
      <linearGradient id="fuel-fill" x1="0" y1="0" x2="0" y2="1">
        <stop offset="0" stop-color="var(--fuel-top)"/>
        <stop offset="1" stop-color="var(--fuel-bottom)"/>
      </linearGradient>
      <linearGradient id="heat-fill" x1="0" y1="0" x2="0" y2="1">
        <stop offset="0" stop-color="var(--heat-top)"/>
        <stop offset="1" stop-color="var(--heat-bottom)"/>
      </linearGradient>
    </defs>

    <g class="grid">
      <line class="grid-line" x1="235" y1="541" x2="975" y2="541"/>
      <line class="grid-line" x1="235" y1="408" x2="975" y2="408"/>
      <line class="grid-line" x1="235" y1="272" x2="975" y2="272"/>
      <line class="grid-line" x1="235" y1="675" x2="975" y2="675"/>
    </g>

    <g class="y-axis">
      <text class="axis-label" x="190" y="154">$400</text>
      <text class="axis-label" x="190" y="279">$300</text>
      <text class="axis-label" x="190" y="415">$200</text>
      <text class="axis-label" x="190" y="548">$100</text>
    </g>

    <!-- Gas furnace -->
    <g class="bar-group">
      <polygon fill="#8cc9dc" points="295,554 305,540 351,540 351,554"/>
      <rect fill="url(#fuel-fill)" x="295" y="554" width="56" height="147"/>
      <text class="bar-label" transform="translate(316 694) rotate(-90)">$100 OF GAS</text>

      <polygon fill="var(--ghost)" points="374,554 380,540 428,540 428,554"/>
      <rect fill="var(--ghost)" opacity="0.85" x="374" y="554" width="54" height="30"/>
      <polygon fill="#f2c4c4" points="374,596 380,583 428,583 428,596"/>
      <rect fill="url(#heat-fill)" x="374" y="596" width="54" height="105"/>
      <text class="bar-label" transform="translate(393 694) rotate(-90)">$80 OF HEAT</text>
    </g>

    <!-- Electric heat -->
    <g class="bar-group">
      <polygon fill="#8cc9dc" points="535,554 545,540 588,540 588,554"/>
      <rect fill="url(#fuel-fill)" x="535" y="554" width="53" height="147"/>
      <text class="bar-label" transform="translate(554 694) rotate(-90)">$100 OF ELECTRICITY</text>

      <polygon fill="#e01a24" points="613,554 616,540 662,540 666,554"/>
      <rect fill="url(#heat-fill)" x="613" y="554" width="53" height="147"/>
      <text class="bar-label" transform="translate(632 694) rotate(-90)">$100 OF HEAT</text>
    </g>

    <!-- Heat pump -->
    <g class="bar-group">
      <polygon fill="#8cc9dc" points="771,554 781,540 829,540 829,554"/>
      <rect fill="url(#fuel-fill)" x="771" y="554" width="58" height="147"/>
      <text class="bar-label" transform="translate(793 694) rotate(-90)">$100 OF ELECTRICITY</text>

      <polygon fill="#e01a24" points="852,151 852,139 902,139 907,151"/>
      <rect fill="url(#heat-fill)" x="852" y="151" width="55" height="550"/>
      <rect fill="#a5121c" opacity="0.5" x="852" y="139" width="3" height="562"/>
      <text class="bar-label bar-label--large" transform="translate(896 540) rotate(-90)">$400 OF HEAT</text>
    </g>

    <g class="categories">
      <text class="category" x="360" y="736">80% efficient Gas Furnace</text>
      <text class="category" x="360" y="759">COP of .8</text>
      <text class="category" x="600" y="736">Electric Heat</text>
      <text class="category" x="600" y="759">COP of 1</text>
      <text class="category" x="846" y="736">Our Best Selling Heat pump</text>
      <text class="category" x="846" y="759">COP of 4 at 47°F</text>
    </g>
  </svg>

  <div class="brand">
    <span class="brand-dot"></span>
    <span class="brand-name">Brightmark Comfort</span>
  </div>

  <div class="callout">
    <span class="callout-bracket callout-bracket--top"></span>
    <span class="callout-bracket callout-bracket--bottom"></span>
    <p class="callout-text">Higher Co-efficient of<br>Performance (COP)<br>means more heat<br>for your money
      <span class="callout-note">*COP measure at 47°F</span></p>
  </div>
</div>
</body>
</html>
```